Postcard Design

Postcard for the following:

Front of postcard:
A new little beauty and health haven has opened up just around the corner at 42 Marston Lane, Fernwood Rise.
Just like you, Mabel’s Lantern is special, offering treatments and services tailor made to your specific needs. Mabel has over 24 years of industry experience and offers a unique approach to helping you feel healthful, nourished and happy. Her treatments are brilliantly effective and include remedial massage therapies and reflexology, gorgeous rejuvenating facials and much much more…………..come and experience this unique and 100% organic little piece of heaven.
You deserve to feel great so we work from the inside out by offering nutritional health advice and formulations developed especially for you. We wholly nourish the individual in the wise woman tradition of healing and happiness.
As a special welcome gift I would like to offer you $15 off any service
By appointment 027 5162930 I look forward to seeing you soon

Back of postcard:
The hearth has been the centre of human life for at least 400,000 years. it is the place where people meet to cook, eat, talk together and heal. The ' hearth' was the heart of the home It was the centre of activity, where everyone gathered to keep warm, laugh, listen to the stories of old and heal. It was the place of physical and emotional nourishment. The hearth is a symbol for the hospitality and living spirit of the home.

Industry/Entity Type

Hospitality

Requirements
Nice to have
• A logo for the business would be really good.

```html
<!DOCTYPE html>
<html lang="en">
<head>
<meta charset="utf-8">
<title>Mabel’s Lantern Postcard</title>
<link rel="stylesheet" href="https://fonts.googleapis.com/css2?family=Fira+Sans:wght@400;500;600;700&family=Aleo:wght@300;400&display=swap">
<style>
  :root {
    --page: #ffffff;
    --front-bg: #f8f0dc;
    --back-bg: #efd5d8;
    --rose: #d9566c;
    --magenta: #e03f94;
    --teal: #1d6f72;
    --teal-bright: #1f9a9a;
    --leaf: #8cc63f;
    --plum: #5a3a48;
    --photo-spa-a: #a9b89a;
    --photo-spa-b: #e2d6b8;
    --photo-skin-a: #e9d2bd;
    --photo-skin-b: #c9b8a6;
    --photo-herb-a: #8b9a55;
    --photo-herb-b: #c89a6a;
  }
  * { box-sizing: border-box; margin: 0; padding: 0; }
  html, body { width: 738px; height: 1200px; overflow: hidden; background: var(--page); }
  body { position: relative; font-family: "Fira Sans", sans-serif; }

  .card { position: absolute; }
  .card--front { left: 25px; top: 38px; width: 693px; height: 537px; background: var(--front-bg); }
  .card--back { left: 25px; top: 608px; width: 697px; height: 540px; background: var(--back-bg); }

  .brand { position: absolute; display: flex; align-items: center; gap: 10px;
    font-family: "Fira Sans", sans-serif; font-weight: 600; font-size: 38px; color: var(--magenta); }
  .brand__dot { width: 16px; height: 16px; border-radius: 50%; background: var(--leaf); }
  .card--front .brand { left: 0; right: 0; top: 34px; justify-content: center; }
  .card--back .brand { left: 40px; top: 36px; }

  .front__headline { position: absolute; left: 43px; top: 120px; width: 365px;
    font-size: 19.5px; font-weight: 500; line-height: 25px; color: var(--rose); }
  .front__body { position: absolute; left: 43px; top: 208px; width: 482px;
    font-size: 13.4px; line-height: 16.8px; color: var(--teal); }
  .front__body-gap { float: right; width: 58px; height: 100px; }
  .front__body p + p { margin-top: 8px; text-indent: 10px; clear: both; }
  .dropcap { font-size: 26px; font-weight: 700; line-height: 14px; color: var(--teal); }

  .photo { position: absolute; }
  .photo--spa { left: 495px; top: 128px; width: 168px; height: 200px; border-radius: 14px;
    background: radial-gradient(circle at 55% 45%, var(--photo-spa-b), var(--photo-spa-a)); }

  .booking { position: absolute; left: 40px; top: 418px; width: 320px; text-align: center;
    font-weight: 700; color: var(--teal-bright); font-size: 18.5px; line-height: 28px; }
  .booking__phone { font-size: 27px; color: var(--rose); line-height: 34px; }

  .offer { position: absolute; left: 378px; top: 418px; width: 260px; text-align: center;
    font-weight: 700; color: var(--leaf); font-size: 18.5px; line-height: 26px; }
  .offer__amount { color: var(--rose); }

  .back__story { position: absolute; left: 40px; top: 112px; width: 352px;
    font-family: "Aleo", serif; font-weight: 300; font-size: 17.4px; line-height: 23.6px; color: var(--plum); }
  .back__story .dropcap { font-family: "Aleo", serif; font-weight: 400; font-size: 27px; color: var(--plum); }

  .photo--stones { left: 393px; top: 85px; width: 277px; height: 264px;
    background: linear-gradient(160deg, #f4efe9, var(--photo-skin-a) 45%, var(--photo-skin-b)); }
  .photo--feet { left: 503px; top: 330px; width: 129px; height: 180px;
    background: linear-gradient(180deg, var(--photo-skin-a), #d8a89a); }
  .strip { position: absolute; left: 40px; top: 385px; width: 392px; height: 122px; display: flex; }
  .strip .photo { position: static; flex: 1; height: 100%; }
  .photo--oil { background: linear-gradient(160deg, #3b3a2a, var(--photo-herb-a)); }
  .photo--drink { background: linear-gradient(160deg, #7a8a50, #e0c7c0); }
  .photo--flowers { background: linear-gradient(160deg, #c2b040, var(--photo-herb-b)); }
  .photo--jars { background: linear-gradient(160deg, #5a3a3a, #b05a6a); }
</style>
</head>
<body>

<section class="card card--front">
  <div class="brand"><span>Mabel’s Lantern</span><span class="brand__dot"></span></div>

  <h1 class="front__headline">A new little beauty and health haven has opened up just around the corner at 42 Marston Lane, Fernwood Rise</h1>

  <div class="photo photo--spa" role="img" aria-label="Spa still life with bath salts, oil and massage stones"></div>

  <div class="front__body">
    <span class="front__body-gap"></span>
    <p><span class="dropcap">J</span>ust like you, Mabel’s Lantern is special, offering treatments and services tailor made to your specific needs. Mabel has over 24 years of industry experience and offers a unique approach to helping you feel healthful, nourished and happy. Her treatments are brilliantly effective and include remedial massage therapies and reflexology, gorgeous rejuvenating facials and much much more . . . come and experience this unique and 100% organic little piece of heaven.</p>
    <p>You deserve to feel great so we work from the inside out by offering nutritional health advice and formulations developed especially for you. We wholly nourish the individual in the wise woman tradition of healing and happiness.</p>
  </div>

  <div class="booking">
    <div>By appointment</div>
    <div class="booking__phone">027 5162930</div>
    <div>I look forward to seeing you soon</div>
  </div>

  <div class="offer">
    <div>As a special welcome gift</div>
    <div>I would like to offer you</div>
    <div><span class="offer__amount">$15 off</span> any service</div>
  </div>
</section>

<section class="card card--back">
  <div class="brand"><span>Mabel’s Lantern</span><span class="brand__dot"></span></div>

  <p class="back__story"><span class="dropcap">T</span>he hearth has been the centre of human life for at least 400,000 years. It is the place where people meet to cook, eat, talk together and heal. The 'hearth' was the heart of the home. It was the centre of activity, where everyone gathered to keep warm, laugh, listen to the stories of old and heal. It was a place of physical and emotional nourishment. The hearth is a symbol for the hospitality and living spirit of the home.</p>

  <div class="photo photo--stones" role="img" aria-label="Hot stone massage on a relaxing client's back"></div>
  <div class="photo photo--feet" role="img" aria-label="Hands giving a reflexology foot massage"></div>

  <div class="strip">
    <div class="photo photo--oil" role="img" aria-label="Pot of herbal oil with pine sprigs"></div>
    <div class="photo photo--drink" role="img" aria-label="Glass of herbal drink with clover flowers"></div>
    <div class="photo photo--flowers" role="img" aria-label="Jar of dandelion flowers infusing"></div>
    <div class="photo photo--jars" role="img" aria-label="Jars of dried flowers and herbs"></div>
  </div>
</section>

</body>
</html>
```